New design and build for natural product Velmarin nosespray

We are looking for a new design for an existing website.

Velmarin is a natural product. we have three types of products. Please have a look at the existing site: velmarin-example.com

We are looking for a natural look and feel. This because the products are 100 procent natural.

We would like to have the following site structure (rows) :
- Picture of a person in nature
- Packshot
- Tekst
- 4 blocks for the four nasal issues with pictures
- Tekst
- 3 blocks with pictures to explain experiences from others.
- I think a need an extra white block with tekst (like this example ‘let your dreams come true’

Please have a look at the attached pdf.
page 2 is a idea where the site structure is important.
page 3 is an existing folder. Idear is to keep the folder look and feel in line with the new site design.
page 4-5-6 Element that are posible.
page 7 design that is too much.

Beside the home page I would like to have a template for the sales page.

The existing site has a large woocommerce customer database. This must stay available.
I have a staging site available where you can build the site. From here we can export and import the new disgn to the production site.

Please make the site in Divi

Requirements
Must have
• Home page and sales page
Nice to have
• see pdf

```html
<!DOCTYPE html>
<html lang="nl">
<head>
<meta charset="utf-8">
<title>Velmarin – Weer vrij ademen door de neus</title>
<link rel="stylesheet" href="https://fonts.googleapis.com/css2?family=Open+Sans:wght@400;600&display=swap">
<style>
:root{
  --green:#6bb545;
  --green-dark:#4f8f31;
  --slate:#4a5663;
  --footer:#2f3e47;
  --ink:#111;
  --muted:#666;
  --grey-bg:#f4f4f4;
  --dream-bg:#e4e3e4;
  --white:#fff;
}
*{box-sizing:border-box;margin:0;padding:0}
html,body{width:1200px;height:2743px;overflow:hidden}
body{font-family:"Open Sans",Arial,sans-serif;color:var(--ink);position:relative;background:var(--white)}
.abs{position:absolute}
.btn{display:inline-block;border-radius:4px;font-size:13px;text-transform:uppercase;padding:8px 16px;line-height:18px}
.btn-green{background:var(--green);color:var(--white);border:1px solid var(--green-dark)}
.btn-white{background:var(--white);color:var(--ink);border:1px solid #222}
.btn-ghost{color:var(--white);border:1.5px solid var(--white);background:var(--green)}
.accent{color:var(--green)}

/* top bar */
.topbar{left:0;top:0;width:1200px;height:37px;background:var(--slate);color:#eee;font-size:13px}
.topbar span{position:absolute;top:9px}
.tick{display:inline-block;vertical-align:-2px;margin-right:4px}
/* header */
.header{left:0;top:37px;width:1200px;height:78px;background:var(--white)}
.brand{left:53px;top:12px;display:flex;align-items:center;gap:8px;font-size:30px;font-weight:600;color:var(--slate)}
.brand i{width:18px;height:18px;background:var(--green);display:block}
.nav a{position:absolute;top:34px;font-size:13px;font-weight:600;color:var(--ink);text-decoration:none}
.shop{left:1070px;top:23px;width:79px;height:36px;background:var(--green);color:var(--white);font-size:13px;font-weight:600;border-radius:4px;text-align:center;line-height:36px}
/* hero */
.hero{left:0;top:115px;width:1200px;height:487px;background:linear-gradient(90deg,#2f6b27 0%,#3f7d30 40%,#5b8f45 70%,#3e6e33 100%)}
.hero h1{left:53px;top:107px;font-size:38px;line-height:47px;font-weight:400;color:var(--white)}
.hero li{position:absolute;list-style:none;color:var(--white);font-size:15px;line-height:19px;left:53px;width:320px}
.packshot{left:388px;top:150px;width:155px;height:325px;background:linear-gradient(180deg,#d92b2b,#b81d1d);border-radius:3px}
.bottle{left:540px;top:205px;width:75px;height:270px;background:linear-gradient(180deg,#f2f2f2,#e7d9a8)}
.person{left:640px;top:0;width:560px;height:487px;background:linear-gradient(180deg,#6f8a5e,#2a2a2a 80%)}
.dots span{position:absolute;top:465px;width:14px;height:14px;border-radius:50%;background:var(--white);opacity:.85}
/* chronic section */
.chronic{left:0;top:602px;width:1200px;height:651px;background:var(--grey-bg)}
.sec-title{width:1200px;left:0;text-align:center;font-size:31px;font-weight:400}
.intro{left:330px;top:127px;width:540px;text-align:center;font-size:12px;line-height:17px;color:var(--muted)}
.issue{top:243px;width:255px;height:342px;background:var(--green);text-align:center;color:var(--ink)}
.issue .pic{height:171px;background:linear-gradient(180deg,#d9d5cf,#b9aea4)}
.issue h3{font-size:14px;font-weight:400;margin-top:26px}
.issue p{font-size:14px;line-height:19px;margin:6px 16px 0;color:#1a1a1a}
.issue .btn{margin-top:20px}
/* dreams */
.dreams{left:0;top:1253px;width:1200px;height:375px;background:var(--dream-bg)}
.leaves{left:0;top:0;width:270px;height:340px;background:radial-gradient(ellipse at 10% 40%,#5ca437 0%,#7cc24a 40%,rgba(228,227,228,0) 70%)}
.frame{left:157px;top:53px;width:222px;height:260px;border-top:8px solid var(--green);border-left:8px solid var(--green)}
.hands{left:165px;top:61px;width:222px;height:260px;background:linear-gradient(180deg,#c9a48f,#4d6a3e 60%,#3a4a30)}
.dreams h2{left:494px;top:54px;font-size:31px;font-weight:400}
.dreams p{left:494px;top:114px;width:655px;font-size:15px;line-height:28.5px;color:var(--muted)}
/* experiences */
.exp-title{top:1695px}
.story{top:1795px;width:342px;height:441px;background:var(--white);box-shadow:0 0 6px rgba(107,181,69,.6)}
.story .pic{height:240px}
.story .date{margin:19px 20px 0;font-size:13px;color:var(--green)}
.story h3{margin:10px 20px 0;font-size:13px;font-weight:600}
.story p{margin:8px 20px 0;font-size:13px;line-height:17px;color:var(--muted)}
.story .btn{margin:23px 20px 0}
/* footer */
.footer{left:0;top:2286px;width:1200px;height:457px;background:var(--footer);color:var(--white)}
.footer h4{position:absolute;top:47px;font-size:13px;font-weight:600;text-transform:uppercase}
.footer .small{font-size:11px;line-height:17px}
.footer .t{position:absolute;font-size:13px;line-height:22px}
.email-field{left:368px;top:163px;width:195px;height:32px;background:var(--white);color:#333;font-size:11px;padding:9px 11px;border-radius:2px}
.divider{left:0;top:293px;width:1200px;height:1px;background:#46545c}
.social span{position:absolute;top:360px;width:33px;height:33px;border-radius:50%;border:2px solid var(--white)}
</style>
</head>
<body>

<div class="abs topbar">
  <span style="left:53px"><svg class="tick" width="12" height="12" viewBox="0 0 12 12"><path d="M1 6l3 3 7-7" stroke="#fff" stroke-width="2" fill="none"/></svg>Op werkdagen besteld de volgend dag verzonden.</span>
  <span style="left:529px"><svg class="tick" width="12" height="12" viewBox="0 0 12 12"><path d="M1 6l3 3 7-7" stroke="#fff" stroke-width="2" fill="none"/></svg>Verzendkosten 2,95 euro in NL</span>
  <span style="left:1010px">Login</span>
  <span style="left:1060px">Cart &nbsp;€ 0.00 <svg width="14" height="12" viewBox="0 0 14 12"><path d="M0 1h3l2 7h7l2-5H4" stroke="#fff" stroke-width="1.6" fill="none"/><circle cx="6" cy="10.5" r="1.3" fill="#fff"/><circle cx="11" cy="10.5" r="1.3" fill="#fff"/></svg></span>
</div>

<header class="abs header">
  <div class="abs brand"><i></i>Velmarin</div>
  <nav class="nav">
    <a style="left:591px">PRODUCT</a>
    <a style="left:705px">EXPERIENCES</a>
    <a style="left:840px">TIPS / INFO</a>
    <a style="left:963px">CONTACT</a>
  </nav>
  <div class="abs shop">SHOP</div>
</header>

<section class="abs hero">
  <div class="abs person" role="img" aria-label="Smiling woman in a green forest"></div>
  <div class="abs packshot" role="img" aria-label="Red product box of the nasal spray"></div>
  <div class="abs bottle" role="img" aria-label="Nasal spray bottle"></div>
  <h1 class="abs">WEER VRJI ADEMEN<br>DOOR DE NEUS</h1>
  <ul>
    <li style="top:231px">🌿&nbsp; Heb je last van loopneus of chronische neusklachten?</li>
    <li style="top:287px">🌿&nbsp; Kom je niet af van je neusspray verslaving?</li>
  </ul>
  <span class="abs btn btn-ghost" style="left:53px;top:350px">Read more</span>
  <div class="dots"><span style="left:576px"></span><span style="left:600px"></span></div>
</section>

<section class="abs chronic">
  <h2 class="abs sec-title" style="top:61px">CHRONISCHE <span class="accent">NEUSKLACHTEN</span></h2>
  <p class="abs intro">Lorem Ipsum is simply dummy text of the printing and typesetting industry. Lorem Ipsum has been the industry's standard dummy text ever since the 1500s, when an unknown printer took a galley</p>
  <div class="abs issue" style="left:53px"><div class="pic" role="img" aria-label="Woman blowing her nose"></div><h3>STUFFY NOSE</h3><p>A stuffy nose is usually the result of a cold.</p><span class="btn btn-white">Read more</span></div>
  <div class="abs issue" style="left:333px"><div class="pic" role="img" aria-label="Man holding his nose bridge"></div><h3>RUNNING NOSE</h3><p>A stuffy nose is usually the result of a cold.</p><span class="btn btn-white">Read more</span></div>
  <div class="abs issue" style="left:614px"><div class="pic" role="img" aria-label="Man with headache from sinusitis"></div><h3>SINUSITIS</h3><p>A stuffy nose is usually the result of a cold.</p><span class="btn btn-white">Read more</span></div>
  <div class="abs issue" style="left:893px"><div class="pic" role="img" aria-label="Woman using a nasal spray"></div><h3>NASAL SPRAY ADDICTION</h3><p>A stuffy nose is usually the result of a cold.</p><span class="btn btn-white">Read more</span></div>
</section>

<section class="abs dreams">
  <div class="abs leaves" role="img" aria-label="Green leaves hanging from the corner"></div>
  <div class="abs frame"></div>
  <div class="abs hands" role="img" aria-label="Cupped hands holding fresh pine sprouts"></div>
  <h2 class="abs">LET YOUR <span class="accent">DREAMS COME TRUE</span></h2>
  <p class="abs">Lorem Ipsum is simply dummy text of the printing and typesetting industry. Lorem Ipsum has been the industry's standard dummy text ever since the 1500s, when an unknown printer took a galley of type and scrambled it to make a type specimen book. It has survived not only five centuries, but also the leap into electronic typesetting, remaining essentially unchanged. It was popularised in the 1960s with the release of Letraset sheets containing</p>
  <span class="abs btn btn-green" style="left:496px;top:283px">Read more</span>
</section>

<h2 class="abs sec-title exp-title">WIL JE MEER LEZEN OVER <span class="accent">ERVARING VAN ANDEREN</span></h2>
<article class="abs story" style="left:55px"><div class="pic" role="img" aria-label="Woman with a tissue at her nose" style="background:linear-gradient(135deg,#e9e2da,#b99485)"></div><div class="date">▦ SEP 3, 2021</div><h3>VERSTOPTE NEUS EN AANHOUDE HOOFDPIJN</h3><p>Lorem Ipsum is simply dummy text of the printing and typesetting industry. Lorem Ipsum has been the industry's standard dummy</p><span class="btn btn-green">Read more</span></article>
<article class="abs story" style="left:428px"><div class="pic" role="img" aria-label="Bearded man with crossed arms" style="background:linear-gradient(180deg,#ececec,#9ec9df)"></div><div class="date">▦ SEP 3, 2021</div><h3>VERSTOPTE NEUS EN AANHOUDE HOOFDPIJN</h3><p>Lorem Ipsum is simply dummy text of the printing and typesetting industry. Lorem Ipsum has been the industry's standard dummy</p><span class="btn btn-green">Read more</span></article>
<article class="abs story" style="left:801px"><div class="pic" role="img" aria-label="Man at a desk looking at his phone" style="background:linear-gradient(135deg,#8a8f94,#e4e2dd)"></div><div class="date">▦ SEP 3, 2021</div><h3>VERSTOPTE NEUS EN AANHOUDE HOOFDPIJN</h3><p>Lorem Ipsum is simply dummy text of the printing and typesetting industry. Lorem Ipsum has been the industry's standard dummy</p><span class="btn btn-green">Read more</span></article>

<footer class="abs footer">
  <svg class="abs" style="left:0;top:-7px" width="1200" height="14"><polygon points="0,14 1200,0 1200,6 0,14" fill="#6bb545"/></svg>
  <h4 style="left:51px">About us</h4>
  <div class="abs brand" style="left:51px;top:87px;color:var(--white);font-size:32px"><i></i>Velmarin</div>
  <p class="abs small" style="left:52px;top:173px;width:205px">Lorem Ipsum is simply dummy text of the printing and typesetting industry. Lorem Ipsum has been the industry's standard dummy</p>

  <h4 style="left:369px">Sign up for news letter</h4>
  <p class="abs small" style="left:370px;top:91px;width:205px">Lorem Ipsum is simply dummy text of the printing and typesetting industry. Lorem Ipsum has been the industry's standard dummy</p>
  <div class="abs email-field">Enter Email</div>
  <span class="abs btn btn-green" style="left:368px;top:229px;padding:7px 16px">Subscribe</span>

  <h4 style="left:679px">Contact us</h4>
  <svg class="abs" style="left:684px;top:87px" width="12" height="15" viewBox="0 0 12 15"><path d="M6 0a6 6 0 0 1 6 6c0 4-6 9-6 9S0 10 0 6a6 6 0 0 1 6-6z" fill="#fff"/><circle cx="6" cy="6" r="2" fill="#2f3e47"/></svg>
  <p class="t" style="left:707px;top:83px">Norvale Care B.V.<br>Lindelaan 17<br>3811 KT Almerveld</p>
  <svg class="abs" style="left:683px;top:170px" width="14" height="14" viewBox="0 0 14 14"><path d="M3 0l3 3-2 2c1 2 3 4 5 5l2-2 3 3-2 3C6 14 0 8 0 2z" fill="#fff"/></svg>
  <p class="t" style="left:707px;top:166px">&nbsp;Phone :<br>+31 (0)20 -555 01 23</p>
  <svg class="abs" style="left:681px;top:222px" width="15" height="12" viewBox="0 0 15 12"><rect x="0" y="0" width="15" height="12" rx="1" fill="#fff"/><path d="M0 1l7.5 6L15 1" stroke="#2f3e47" stroke-width="1.5" fill="none"/></svg>
  <p class="t" style="left:707px;top:218px">&nbsp;Email :<br>info@velmarin-example.com</p>

  <h4 style="left:988px">International</h4>
  <p class="t" style="left:986px;top:83px">Frankrijk: velmarin-example.fr</p>
  <p class="t" style="left:986px;top:128px">Engeland: velmarin-example.co.uk</p>
  <p class="t" style="left:986px;top:173px">Spanje: velmarin-example.es</p>

  <div class="abs divider"></div>
  <p class="abs" style="left:0;width:1200px;text-align:center;top:311px;font-size:13px">Copyright 2021 © Velmarin.</p>
  <div class="social" aria-label="Social media links"><span style="left:537px"></span><span style="left:579px"></span><span style="left:620px"></span></div>
</footer>

</body>
</html>
```